Outdoor group fitness training - Greta Moxley Personal Training

I want an eye catching A4 flyer that promotes my two outdoor fitness groups. I have uploaded photos of each location: Mylor and Pasadena.
The target group is existing and potential new Personal training clients - all adults. There are two morning groups at Mylor ; one evening and one morning group at Pasadena. The groups will be for up to 8 people and are for all fitness levels.I want to encourage people to come and have a go. I have also uploaded a design I have used through printhollow for a previous flyer. I would like to use the orange graphic of the two people at the bottom of this design.
Cost is $15 per person
Location and times - Brackenridge Oval Wednesdays 7.30am; Sundays 8am
Corvale High School Thursdays 6.30pm: Saturdays 8am
Updates

Thanks so much to all of you for submitting a great set of designs. it was really hard making a choice in the end, and I really appreciate the promptness and creativity that went into the designs. I will certainly keep you in mind for future jobs. Cheers and have a great day Greta Moxley

Target Market(s)

40 - 60 year old adults: cross section of professionals, tradespeople and retirees. People who will enjoy socialising while also getting fit. No extremely fit people - cross section of beginners to intermediate; males and females

Industry/Entity Type

Training

Font styles to use
Sans Serif

Colors
f78f20
9bcb3c
ecf7fb

Requirements
Must have
• Fast turnaround required - within two days
Bright and attention grabbing, engaging. Could be A4 or could be postcard size?

State cost clearly
State that first 5 people to join either group will get first session at half price

```html
<!DOCTYPE html>
<html lang="en">
<head>
<meta charset="utf-8">
<title>Greta Moxley Personal Training – Outdoor Group Fitness</title>
<link rel="stylesheet" href="https://fonts.googleapis.com/css2?family=Arimo:wght@700&family=Open+Sans:wght@400&display=swap">
<style>
  :root {
    --stage: #e9ecee;
    --frame: #f78f20;
    --lime: #8cff00;
    --title: #f78f20;
    --ink: #ffffff;
    --offer: #e3120b;
    --photo-light: #d99a62;
    --photo-mid: #a8683a;
    --photo-dark: #4e3a2c;
  }
  * { margin: 0; padding: 0; box-sizing: border-box; }
  html, body {
    width: 1200px; height: 982px; overflow: hidden;
    background: var(--stage);
  }
  .flyer {
    position: absolute; left: 270px; top: 41px;
    width: 660px; height: 900px;
    background: var(--frame);
    padding: 14px;
  }
  .flyer-body {
    position: relative; width: 632px; height: 872px; overflow: hidden;
    font-family: "Open Sans", sans-serif; color: var(--ink);
  }
  .backdrop { position: absolute; inset: 0; width: 632px; height: 872px; }
  .trainer-name {
    position: absolute; top: 22px; right: 34px;
    font-family: "Arimo", sans-serif; font-weight: 700;
    font-size: 60px; color: var(--title); letter-spacing: -0.5px;
  }
  .promo {
    position: absolute; left: 28px; top: 122px; width: 270px;
    text-align: center; font-size: 28px; line-height: 1.22;
  }
  .promo .highlight { color: var(--offer); }
  .features {
    position: absolute; right: 30px; top: 122px; width: 290px;
    text-align: right; font-size: 22px; line-height: 1.25;
  }
  .features p + p { margin-top: 24px; }
  .cost {
    position: absolute; left: 38px; top: 346px; font-size: 27px;
  }
  .schedule-heading {
    position: absolute; left: 38px; top: 398px; font-size: 22px;
  }
  .venue {
    position: absolute; left: 38px; font-size: 16px; line-height: 1.3;
  }
  .venue-oval { top: 462px; }
  .venue-school { top: 560px; }
</style>
</head>
<body>
  <main class="flyer">
    <div class="flyer-body">
      <svg class="backdrop" viewBox="0 0 632 872" aria-hidden="false">
        <defs>
          <linearGradient id="photoTone" x1="0" y1="0" x2="1" y2="1">
            <stop offset="0" stop-color="var(--photo-light)"/>
            <stop offset="0.5" stop-color="var(--photo-mid)"/>
            <stop offset="1" stop-color="var(--photo-dark)"/>
          </linearGradient>
        </defs>
        <rect role="img" aria-label="Sepia-orange photo of two people running along a seaside path" x="0" y="480" width="632" height="392" fill="url(#photoTone)"/>
        <path d="M0 0 H632 V500 C560 515 470 540 370 578 C250 622 130 640 0 672 Z" fill="var(--lime)"/>
      </svg>

      <h1 class="trainer-name">Greta Moxley</h1>

      <p class="promo">First 5 people to join either group will get first session at <span class="highlight">half price!</span></p>

      <div class="features">
        <p>Up to 8 people per group.</p>
        <p>Beginners to intermediate.</p>
        <p>Males and Females are all welcome!</p>
        <p>Enjoy socialising while getting fit at the same time</p>
      </div>

      <p class="cost">Cost is $15 per person</p>
      <p class="schedule-heading">Location and time:</p>
      <p class="venue venue-oval">Brackenridge Oval<br>Wednesdays 7.30am<br>Sundays 8am</p>
      <p class="venue venue-school">Corvale High School<br>Thursdays 6.30pm Saturdays 8am</p>
    </div>
  </main>
</body>
</html>
```